VornaRank.com

We need a new web design for our seo services website at vornarank.com.

Right now we have our homepage, and 2 other pages which we use a html code generator. We need a header and footer and a nice professional looking design to showcase our seo plans.

As for the logo we'll use our company vornaforge.com logo Vorna and change Work to Submit and Technologies to Search Engine Marketing.

We also like to display our textfountain widget and author alert sign up box.

Industry/Entity Type

It Company

Requirements

```html
<!DOCTYPE html>
<html lang="en">
<head>
<meta charset="utf-8">
<title>VornaRank – Organic SEO Plans</title>
<link rel="stylesheet" href="https://fonts.googleapis.com/css2?family=Roboto:wght@400;500;700&display=swap">
<style>
:root{
  --navy:#0e2c78;
  --navy-dark:#0a2163;
  --red:#d7101c;
  --gold:#f6bd22;
  --silver:#c3cbcc;
  --grey-head:#b4b4b4;
  --ink:#222;
  --body:#444;
  --line:#dcdcdc;
  --panel:#2b2b2b;
  --footer:#333;
  --footer-bar:#222;
  --soft:#e9e9e9;
}
*{box-sizing:border-box;margin:0;padding:0}
html,body{width:951px;height:1200px;overflow:hidden;background:#fff}
body{font-family:Roboto,Arial,sans-serif;color:var(--ink);position:relative}
.wrap{position:absolute;left:97px;width:757px}

/* header */
.site-header{top:0;height:100px}
.logo{position:absolute;left:0;top:26px;display:flex;align-items:center;gap:8px}
.logo-mark{width:22px;height:22px;border-radius:50%;background:var(--red)}
.logo-name{font-size:30px;font-weight:700;color:var(--navy);letter-spacing:-.5px}
.tagline{position:absolute;left:310px;width:210px;top:32px;text-align:center;color:var(--navy);font-size:16.5px;line-height:20px}
.call{position:absolute;right:0;top:33px;text-align:right}
.call small{display:block;font-size:10px;color:#888}
.call strong{display:block;font-size:19.5px;color:var(--red);font-weight:700;margin-top:3px}

/* nav */
.main-nav{top:104px;height:29px;display:flex;background:var(--navy);border-radius:3px;overflow:hidden}
.main-nav a{height:29px;line-height:29px;text-align:center;color:#fff;font-size:10.5px;text-decoration:none;border-right:1px solid #0a1f57}
.main-nav a:last-child{border-right:0}
.main-nav a.active{background:var(--red)}

/* plans */
.plans-title{top:148px;text-align:center;font-size:23px;font-weight:400;color:var(--navy)}
.plans-title span{color:var(--red)}
.plans{top:193px;display:flex;justify-content:space-between}
.plan{width:176px;height:180px;background:#fff;box-shadow:0 2px 6px rgba(0,0,0,.12);border-radius:3px 3px 0 0;text-align:center;position:relative}
.plan::after{content:"";position:absolute;left:14px;right:14px;bottom:-6px;height:6px;border-radius:50%;background:rgba(0,0,0,.18);filter:blur(2px)}
.plan-name{height:30px;line-height:30px;font-size:16px;color:#222}
.silver .plan-name{background:var(--silver)}
.gold .plan-name{background:var(--gold)}
.grey .plan-name{background:var(--grey-head)}
.plan-price{height:66px;padding-top:18px;border-bottom:1px solid var(--line);color:var(--navy);font-size:14px}
.plan-price sup{font-size:16px;vertical-align:12px}
.plan-price b{font-size:29px;font-weight:400;color:var(--red)}
.plan-keys{height:28px;line-height:27px;border-bottom:1px solid var(--line);font-size:10.5px}
.quote-btn{display:inline-flex;align-items:center;justify-content:space-between;width:114px;height:31px;margin-top:13px;padding:0 7px 0 9px;background:#1c1c1c;border-radius:3px;color:#fff;font-size:10px;font-weight:500;line-height:11px;text-align:left;text-decoration:none}
.quote-btn svg{flex:none}

/* services */
.services{position:absolute;left:97px;top:416px;width:520px;height:573px;border:1px solid var(--line);border-radius:3px;display:grid;grid-template-columns:261px 1fr;grid-template-rows:185px 202px 1fr}
.service{padding:16px 22px 0;border-bottom:1px solid var(--line);position:relative}
.service:nth-child(odd){border-right:1px solid var(--line)}
.service:nth-child(n+5){border-bottom:0}
.service h3{font-size:19.5px;font-weight:400;color:var(--navy);line-height:22px}
.service .term{font-size:12px;color:var(--red);line-height:14px}
.service p{margin-top:16px;font-size:9.9px;line-height:12px;color:var(--body);text-align:justify}
.details-btn{position:absolute;left:22px;bottom:28px;width:87px;height:24px;line-height:24px;text-align:center;background:var(--navy);color:#fff;font-size:10.5px;border-radius:3px;text-decoration:none}
.service.tall .details-btn{bottom:31px}

/* sidebar */
.articles{position:absolute;left:643px;top:415px;width:211px;height:245px;background:var(--panel);border-radius:3px;padding:9px 8px}
.articles h4{font-size:14px;font-weight:400;color:#fff;margin:0 0 9px 1px}
.articles h4 b{font-weight:700}
.article-list{background:#fff;border-radius:2px;padding:5px 11px 0;height:200px}
.article{padding:7px 0 9px;font-size:9.9px;line-height:12px;color:var(--body)}
.article + .article{border-top:1px solid var(--line)}
.article h5{font-size:10px;color:var(--navy);font-weight:700;margin-bottom:6px;line-height:12px}
.article a{display:block;margin-top:7px;color:var(--red);font-weight:700;text-decoration:none}

.alerts{position:absolute;left:643px;top:680px;width:211px;height:220px;background:var(--soft);border-radius:3px;padding:9px 8px}
.alerts h4{font-size:11px;font-weight:400;color:var(--navy);line-height:13px;margin-left:5px}
.alerts h4 b{font-weight:700}
.alerts h4 span{color:var(--red)}
.alert-form{margin-top:7px;background:#fff;height:168px;padding:10px 9px;font-size:9.9px;color:var(--body);line-height:12px}
.alert-form a{color:var(--navy)}
.field{display:flex;align-items:center;justify-content:space-between;margin-top:14px}
.field:first-of-type{margin-top:16px}
.field input{width:136px;height:20px;border:1px solid #ccc;border-radius:3px}
.signup{display:block;margin:13px 0 0 46px;width:60px;height:23px;background:var(--navy);color:#fff;border:0;border-radius:3px;font:10.5px Roboto,Arial,sans-serif}

/* footer */
.site-footer{top:1013px;height:162px;background:var(--footer);border-radius:3px;color:#fff;overflow:hidden}
.footer-col{position:absolute;top:14px}
.footer-col h4{font-size:15.5px;font-weight:400;margin-bottom:12px}
.footer-col ul{list-style:none;font-size:10px;line-height:18px}
.footer-col li::before{content:"";display:inline-block;width:4px;height:4px;border-radius:50%;background:#fff;margin:0 6px 2px 1px}
.divider{position:absolute;top:23px;width:1px;height:104px;background:#555}
.social li{display:flex;align-items:center;gap:11px;height:24px;font-size:10.5px}
.social li::before{display:none}
.social i{width:18px;height:18px;border-radius:50%;background:#6fa2c9}
.quote{font-size:10px;line-height:12px;width:200px;position:relative;padding:8px 0 0 3px}
.quote .mark{position:absolute;font-size:20px;color:#888;font-weight:700}
.quote .open{left:0;top:0}
.quote .close{right:-6px;top:22px}
.quote p{text-indent:22px}
.quote cite{display:block;font-style:normal;margin-top:14px;color:#ccc}
.quote cite b{color:#fff}
.more{position:absolute;right:15px;top:139px;font-size:10px;font-weight:700;color:#fff}
.footer-bar{position:absolute;left:0;right:0;bottom:0;height:25px;line-height:25px;background:var(--footer-bar);text-align:center;font-size:10px}
</style>
</head>
<body>

<header class="wrap site-header">
  <div class="logo"><span class="logo-mark"></span><span class="logo-name">VornaForge</span></div>
  <div class="tagline">Live Rank Tracking,<br>Reports &amp; Much More</div>
  <div class="call"><small>Feel Free &amp; Call Us</small><strong>555 012 347</strong></div>
</header>

<nav class="wrap main-nav">
  <a class="active" style="width:73px">Home</a>
  <a style="width:91px">Services</a>
  <a style="width:110px">Case Studies</a>
  <a style="width:113px">Pricing Model</a>
  <a style="width:93px">About Us</a>
  <a style="width:109px">Testimonials</a>
  <a style="width:76px">Blog</a>
  <a style="width:92px">Contact Us</a>
</nav>

<h1 class="wrap plans-title">Organic <span>SEO</span> Plans</h1>

<section class="wrap plans">
  <div class="plan silver">
    <div class="plan-name">Silver</div>
    <div class="plan-price"><sup>$</sup> <b>500</b> / month</div>
    <div class="plan-keys">Up to <b>10</b> Keywords</div>
    <a class="quote-btn">REQUEST A<br>FREE QOUTE<svg width="24" height="24" viewBox="0 0 24 24"><circle cx="12" cy="12" r="12" fill="#fff"/><path d="M10 7l5 5-5 5" stroke="#0e2c78" stroke-width="2.6" fill="none"/></svg></a>
  </div>
  <div class="plan gold">
    <div class="plan-name">Gold</div>
    <div class="plan-price"><sup>$</sup> <b>750</b> / month</div>
    <div class="plan-keys">Up to <b>20</b> Keywords</div>
    <a class="quote-btn">REQUEST A<br>FREE QOUTE<svg width="24" height="24" viewBox="0 0 24 24"><circle cx="12" cy="12" r="12" fill="#fff"/><path d="M10 7l5 5-5 5" stroke="#0e2c78" stroke-width="2.6" fill="none"/></svg></a>
  </div>
  <div class="plan grey">
    <div class="plan-name">Platinum</div>
    <div class="plan-price"><sup>$</sup><b>1200</b> / month</div>
    <div class="plan-keys">Up to <b>30</b> Keywords</div>
    <a class="quote-btn">REQUEST A<br>FREE QOUTE<svg width="24" height="24" viewBox="0 0 24 24"><circle cx="12" cy="12" r="12" fill="#fff"/><path d="M10 7l5 5-5 5" stroke="#0e2c78" stroke-width="2.6" fill="none"/></svg></a>
  </div>
  <div class="plan grey">
    <div class="plan-name">Platinum Plus</div>
    <div class="plan-price"><sup>$</sup><b>1300</b> / month</div>
    <div class="plan-keys">Up to <b>40</b> Keywords</div>
    <a class="quote-btn">REQUEST A<br>FREE QOUTE<svg width="24" height="24" viewBox="0 0 24 24"><circle cx="12" cy="12" r="12" fill="#fff"/><path d="M10 7l5 5-5 5" stroke="#0e2c78" stroke-width="2.6" fill="none"/></svg></a>
  </div>
</section>

<section class="services">
  <article class="service">
    <h3>Website Audit</h3><div class="term">month 1 setup</div>
    <p>Insightful audits that help you understand what work needs to be done and what the website can rank for. Our comprehensive site audit maximizes the effects of our methodology.</p>
    <a class="details-btn">VIEW DETAILS</a>
  </article>
  <article class="service">
    <h3>Website Optimization</h3><div class="term">month 1 setup</div>
    <p>Starting with your website, we will optimize all key aspects of its targeted pages. Our optimization process ensures your website will be ready to rank once we begin our off-page marketing efforts.</p>
    <a class="details-btn">VIEW DETAILS</a>
  </article>
  <article class="service tall">
    <h3>Rich Searchly Listing</h3><div class="term">month 1 setup</div>
    <p>We'll advise you on how to get the best listing you can in the search results pages. These types of listings get more clicks because of the dynamic information.</p>
    <a class="details-btn">VIEW DETAILS</a>
  </article>
  <article class="service tall">
    <h3>Citation &amp; Link Building</h3><div class="term">month 1 setup</div>
    <p>Starting with your website, we will optimize all key aspects of its targeted pages. Our optimization process ensures your website will be ready to rank once we begin our off-page marketing efforts.</p>
    <a class="details-btn">VIEW DETAILS</a>
  </article>
  <article class="service">
    <h3>Content Marketting</h3><div class="term">ongoing monthly campaign</div>
    <p>We'll start getting the word out about your business quickly. In Month 1 we do things like Press Releases, Magazine Features, and Social Sharing.</p>
    <a class="details-btn">VIEW DETAILS</a>
  </article>
  <article class="service">
    <h3>Reporting &amp; Strategy</h3><div class="term">monthly</div>
    <p>Our live dashboard always has up to date traffic information and search results rankings. You can log in at any time, or get a comprehensive PDF report showing rankings and traffic.</p>
    <a class="details-btn">VIEW DETAILS</a>
  </article>
</section>

<aside class="articles">
  <h4>Articles by <b>Daniel Okafor</b></h4>
  <div class="article-list">
    <div class="article">
      <h5>Different Kinds of Internet Marketing</h5>
      Internet marketing is a very diverse and growing and field. There are many different paths ...
      <a>continue</a>
    </div>
    <div class="article">
      <h5>Seven Ways to Promote Your<br>New Website</h5>
      Thousands of web pages are being added to the Internet daily. If you want your ...
      <a>continue</a>
    </div>
  </div>
</aside>

<aside class="alerts">
  <h4><b>Daniel Okafor's</b> Expert Author<br><span>Email Alerts</span></h4>
  <form class="alert-form">
    Sign up to receive email alerts of<br><b>Daniel Okafor's</b> latest articles from<br><a>TextFountain.com!</a>
    <label class="field">Name :<input type="text"></label>
    <label class="field">Email :<input type="text"></label>
    <button class="signup" type="button">SIGNUP</button>
  </form>
</aside>

<footer class="wrap site-footer">
  <div class="footer-col" style="left:15px">
    <h4>Quick Links</h4>
    <ul><li>Services</li><li>Case Studies</li><li>Pricing Model</li></ul>
  </div>
  <span class="divider" style="left:140px"></span>
  <div class="footer-col" style="left:184px">
    <h4>Quick Links</h4>
    <ul><li>About Us</li><li>Testimonials</li><li>Blog</li><li>Contact Us</li></ul>
  </div>
  <span class="divider" style="left:313px"></span>
  <div class="footer-col" style="left:370px">
    <h4>Follow Us</h4>
    <ul class="social"><li><i></i>Friendspace</li><li><i></i>Chirper</li><li><i></i>Linkwork</li></ul>
  </div>
  <span class="divider" style="left:497px"></span>
  <div class="footer-col" style="left:529px">
    <h4>Testimonials</h4>
    <blockquote class="quote">
      <span class="mark open">“</span>
      <p>Lorem ipsum dolor sit amet, consectetur adipisicing elit, sed do eiusmod tempor incididunt ut labore et dolore magna aliqua ...</p>
      <span class="mark close">”</span>
      <cite><b>Peter</b>, 18/09/13</cite>
    </blockquote>
  </div>
  <a class="more">more</a>
  <div class="footer-bar">Copyright © 2013 <b>VornaSubmit Internet Marketing Service</b>. All rights reserved.</div>
</footer>

</body>
</html>
```